Celebrity News Site

We need a new 1 Page (homepage) layout for a new website we are developing. It will be coded "responsive" to work on both larger and smaller screens.

We like the colors (bright and lots of white) from these sites: http://www.brightlanepost.example www.velmarigazette.example

We like a narrow navigation across the top, preferibly with a black background.

The site will mostly be made up of photos and ads.

I've done a sample layout. And attached our logo.
Updates

Sorry if there was any confusion. I just need one page (homepage) design. Not a full site. Added Tuesday, February 7, 2017

Target Market(s)

USA

Industry/Entity Type

News

Number of Pages Required

1 page

Colors
e34197
eea4c8
ffffff
f59195
f04a50
ec1f27

Requirements
Must have
• Thin, black nav bar at the top.
Nice to have
• Bright colors, white background
Should not have
• some of the bright colors I listed below.

```html
<!DOCTYPE html>
<html lang="en">
<head>
<meta charset="utf-8">
<title>fameLUX — Find your favourite celebrity and athletes</title>
<link href="https://fonts.googleapis.com/css2?family=Raleway:wght@300;400;500;600;700;800&display=swap" rel="stylesheet">
<style>
  :root {
    --black: #0b0b0c;
    --pink: #ef6aa8;
    --pink-deep: #e34197;
    --blue: #3ab0e6;
    --page: #eeeeee;
    --white: #ffffff;
    --ad-grey: #7d7d7d;
    --label-grey: #a6a6a6;
    --icon-grey: #6f6f6f;
    --hero-dark: #3d2a2e;
  }
  * { box-sizing: border-box; margin: 0; padding: 0; }
  html, body { width: 876px; height: 1200px; overflow: hidden; }
  body {
    position: relative;
    font-family: "Raleway", sans-serif;
    background: var(--page);
    color: #333;
  }
  .abs { position: absolute; }

  /* Top bar */
  .topbar { left: 0; top: 0; width: 876px; height: 34px; background: var(--black); }
  .brand { font-family: "Raleway", sans-serif; font-weight: 800; color: var(--pink); letter-spacing: -0.3px; }
  .topbar .brand { left: 119px; top: 5px; font-size: 20px; }
  .search { left: 249px; top: 10px; width: 209px; height: 15px; background: var(--white); border-radius: 3px; }
  .search span { position: absolute; left: 9px; top: 2px; font-size: 6.5px; font-style: italic; color: #aaa; }
  .search svg { position: absolute; right: 6px; top: 3px; }
  .nav { top: 13px; font-size: 7.5px; font-weight: 500; color: var(--white); letter-spacing: 0.1px; }
  .nav.active { color: var(--pink); }
  .menu-icon { left: 772px; top: 12px; }

  /* Hero */
  .hero-bg {
    left: 0; top: 34px; width: 876px; height: 371px;
    background:
      radial-gradient(circle at 560px 190px, #e9c7bd 0, #b88a86 60px, #6b4a4d 140px, transparent 240px),
      radial-gradient(circle at 230px 40px, #b2614d 0, #6a3a36 110px, transparent 200px),
      linear-gradient(180deg, #4a3236 0%, var(--hero-dark) 100%);
  }
  .hero-panel { left: 111px; top: 102px; width: 386px; height: 225px; background: rgba(48, 34, 38, 0.72); }
  .hero-title { left: 118px; top: 109px; width: 380px; font-size: 21.5px; line-height: 26px; font-weight: 800; color: var(--white); }
  .hero-copy { left: 119px; top: 171px; width: 360px; font-size: 11px; line-height: 16.5px; color: #ddd2d2; }
  .btn-hero {
    left: 120px; top: 260px; width: 189px; height: 44px; border-radius: 22px;
    background: var(--pink); color: var(--white); font-size: 10.5px; font-weight: 500;
    display: flex; align-items: center; justify-content: center;
  }

  /* Ads */
  .ad { background: var(--ad-grey); color: var(--white); font-weight: 300; display: flex; align-items: center; box-shadow: 0 1px 2px rgba(0,0,0,0.18); }
  .ad-wide { width: 438px; height: 65px; font-size: 54px; letter-spacing: -0.5px; }
  .ad-side { left: 566px; top: 618px; width: 216px; height: 65px; background: var(--white); color: #7a7a7a; font-size: 30px; padding-left: 8px; }
  .ad-label { font-size: 6.5px; color: var(--label-grey); letter-spacing: 0.2px; }

  /* Person grid */
  .tile { width: 137px; height: 137px; box-shadow: 0 1px 2px rgba(0,0,0,0.2); }
  .tone-a { background: radial-gradient(circle at 55% 40%, #8a5b3e 0, #5d4430 35%, #c9c02d 70%, #8d9a2a 100%); }
  .tone-b { background: radial-gradient(circle at 50% 35%, #d5a287 0, #b78a71 30%, #9ea6ab 55%, #24324f 80%, #1d2740 100%); }
  .tone-c { background: radial-gradient(circle at 50% 45%, #d9a68c 0, #b48062 28%, #7b5a3e 55%, #a08566 80%, #e6e1dc 100%); }
  .tile-hover { background: radial-gradient(circle at 50% 55%, #3a3222 0, #2b2a18 50%, #1c1c12 100%); }
  .tile-name { left: 117px; top: 512px; width: 137px; text-align: center; font-size: 9.5px; line-height: 14px; font-weight: 700; color: var(--blue); }
  .tile-btn { left: 148px; top: 616px; width: 71px; height: 18px; border: 1px solid var(--pink); color: var(--pink); font-size: 7px; display: flex; align-items: center; justify-content: center; }

  .btn-more {
    left: 117px; top: 958px; width: 438px; height: 34px; border-radius: 7px;
    background: var(--pink); color: var(--white); font-size: 7.5px; font-weight: 700;
    display: flex; align-items: center; justify-content: center;
  }

  /* Bio card */
  .bio-card {
    left: 566px; top: 421px; width: 216px; height: 188px;
    background: radial-gradient(circle at 60% 30%, #5b5426 0, #2a2a1c 40%, #111112 80%);
  }
  .bio-name { left: 582px; top: 430px; font-size: 10px; font-weight: 700; color: var(--blue); }
  .bio-sub { left: 583px; top: 443px; font-size: 7px; font-weight: 700; color: var(--white); }
  .bio-copy { left: 590px; top: 483px; width: 168px; text-align: center; font-size: 7.5px; line-height: 13.6px; font-weight: 600; color: var(--white); }
  .bio-btn { left: 641px; top: 580px; width: 78px; height: 20px; background: var(--pink); color: var(--white); font-size: 7px; font-weight: 600; display: flex; align-items: center; justify-content: center; }

  /* Social */
  .social-head { left: 566px; top: 711px; width: 216px; height: 24px; background: var(--pink); color: var(--white); font-size: 7.5px; font-weight: 700; display: flex; align-items: center; justify-content: center; }
  .social-body { left: 566px; top: 735px; width: 216px; height: 51px; background: var(--white); box-shadow: 0 1px 2px rgba(0,0,0,0.15); display: flex; justify-content: center; align-items: center; gap: 9px; }
  .social-body span { width: 26px; height: 26px; border-radius: 5px; background: var(--icon-grey); }

  /* Footer */
  .footer { left: 0; top: 1151px; width: 876px; height: 49px; background: var(--black); }
  .footer .brand { left: 119px; top: 1163px; font-size: 20px; }
  .foot-link { top: 1171px; font-size: 7.5px; color: #e6e6e6; font-weight: 500; }
  .copyright { left: 560px; top: 1171px; width: 221px; text-align: right; font-size: 6.5px; color: #2f2f2f; }
</style>
</head>
<body>

  <header>
    <div class="abs topbar"></div>
    <div class="abs brand">fameLUX</div>
    <div class="abs search">
      <span>Search for your favourite celebrity or athletes...</span>
      <svg width="8" height="8" viewBox="0 0 8 8"><circle cx="3.2" cy="3.2" r="2.3" fill="none" stroke="#ef6aa8" stroke-width="1.1"/><line x1="5" y1="5" x2="7.3" y2="7.3" stroke="#ef6aa8" stroke-width="1.2"/></svg>
    </div>
    <nav>
      <span class="abs nav active" style="left:586px">WELCOME</span>
      <span class="abs nav" style="left:641px">CELEBRITY SEARCH</span>
      <span class="abs nav" style="left:729px">CONTACT</span>
      <svg class="abs menu-icon" width="10" height="9" viewBox="0 0 10 9"><rect y="0" width="10" height="1.8" fill="#fff"/><rect y="3.6" width="10" height="1.8" fill="#fff"/><rect y="7.2" width="10" height="1.8" fill="#fff"/></svg>
    </nav>
  </header>

  <section class="hero">
    <div class="abs hero-bg" role="img" aria-label="Photo of a hand holding a lit sparkler against a dark background"></div>
    <div class="abs hero-panel"></div>
    <h1 class="abs hero-title">FIND YOU FAVOURITE CELEBRITY AND ATHLETES</h1>
    <p class="abs hero-copy">Lorem ipsum dolor sit amet, consectetur adipisicing elit, sed do eius-mod tempor incididunt ut labore et dolore magna aliqua. Ut enim ad minim veniam, quis nostrud exercitation ullamco laboris nisi ut. aliquip. ex ea commodo consequat. Duis aute irure dolor in .</p>
    <div class="abs btn-hero">START SEARCHING</div>
  </section>

  <main>
    <div class="abs ad ad-wide" style="left:117px;top:421px;padding-left:15px">YOUR AD HERE</div>
    <div class="abs ad-label" style="left:118px;top:488px">ADVERTISEMENT</div>

    <div class="abs tile tile-hover" style="left:117px;top:506px" role="img" aria-label="Photo of a footballer in a yellow jersey celebrating, dimmed"></div>
    <div class="abs tile-name">MARCO SILVEIRA<br>DUARTE</div>
    <div class="abs tile-btn">READ BIO</div>
    <div class="abs tile tone-b" style="left:267px;top:506px" role="img" aria-label="Portrait photo of a swimmer wearing a medal"></div>
    <div class="abs tile tone-c" style="left:418px;top:506px" role="img" aria-label="Portrait photo of a smiling woman with long hair"></div>

    <div class="abs tile tone-a" style="left:117px;top:658px" role="img" aria-label="Photo of a footballer in a yellow jersey celebrating"></div>
    <div class="abs tile tone-b" style="left:267px;top:658px" role="img" aria-label="Portrait photo of a swimmer wearing a medal"></div>
    <div class="abs tile tone-c" style="left:418px;top:658px" role="img" aria-label="Portrait photo of a smiling woman with long hair"></div>

    <div class="abs tile tone-a" style="left:117px;top:808px" role="img" aria-label="Photo of a footballer in a yellow jersey celebrating"></div>
    <div class="abs tile tone-b" style="left:267px;top:808px" role="img" aria-label="Portrait photo of a swimmer wearing a medal"></div>
    <div class="abs tile tone-c" style="left:418px;top:808px" role="img" aria-label="Portrait photo of a smiling woman with long hair"></div>

    <div class="abs btn-more">SEE MORE PEOPLE</div>

    <div class="abs ad ad-wide" style="left:117px;top:1012px;justify-content:center;font-size:46px">YOUR AD HERE</div>
    <div class="abs ad-label" style="left:118px;top:1079px">ADVERTISEMENT</div>
  </main>

  <aside>
    <div class="abs bio-card" role="img" aria-label="Photo of a sprinter in a yellow and green kit, darkened behind bio text"></div>
    <div class="abs bio-name">DORIAN KEMP <svg width="5" height="6" viewBox="0 0 5 6" style="margin-left:3px"><path d="M0 0 L4 3 L0 6 Z" fill="#fff"/></svg></div>
    <div class="abs bio-sub">BIO</div>
    <p class="abs bio-copy">Lorem ipsum dolor sit amet, consectetur adipisicing elit, sed do eiusmod tempor incididunt ut labore et dolore magna aliqua. Ut enim ad minim veniam, quis nostrud exercitation ullamco laboris nisi ut aliquip ex ea commodo consequat.</p>
    <div class="abs bio-btn">READ FULL BIO</div>

    <div class="abs ad ad-side">YOUR AD HERE</div>
    <div class="abs ad-label" style="left:570px;top:686px">ADVERTISEMENT</div>

    <div class="abs social-head">FIND US ON SOCIAL MEDIA</div>
    <div class="abs social-body">
      <span></span><span></span><span></span><span></span><span></span>
    </div>
  </aside>

  <footer>
    <div class="abs footer"></div>
    <div class="abs brand">fameLUX</div>
    <span class="abs foot-link" style="left:234px">HOME</span>
    <span class="abs foot-link" style="left:269px">SEARCH</span>
    <span class="abs foot-link" style="left:311px">FAQ</span>
    <span class="abs foot-link" style="left:338px">PRIVACY/POLICY</span>
    <span class="abs foot-link" style="left:412px">CONTACT</span>
    <span class="abs copyright">Copyright 2017 fameLUX. All rights reserved.</span>
  </footer>

</body>
</html>
```